New Mechanical Maintenance business needs website

New Mechanical Maintenance business in Perth Western Australia needs a nice and easy to navigate website. Showing what we do and how we can be the right fit for other small to medium size business by offering personalized service from our highly skilled team. We deal with both fixed plant repairs like food and chemical processing facilities to heavy equipment like drill rigs, Large boats and earthmoving equipment.

Target Market(s)

Small to medium business to offer personalized services/packages

Industry/Entity Type

e deal with both fixed plant repairs like food and chemical processing facilities to heavy equipment like drill rigs, Large boats and earthmoving equipment.

Coding

Coded - Design and coding required

Number of Pages Required

4 page

Font styles to use
Serif

Colors
0054AA
0677BA
7BADD7
CADEEF
E8F1F8

Requirements
Must have
• A website that is easy to navigate but covers off on the range of services/maintenance we can provide

```html
<!DOCTYPE html>
<html lang="en">
<head>
<meta charset="utf-8">
<title>Kestrel Works Maintenance — Mechanical Instrumentation Services</title>
<link rel="stylesheet" href="https://fonts.googleapis.com/css2?family=Poppins:wght@400;500;600;700;800&display=swap">
<style>
:root{
  --slate:#55678a;
  --slate-dark:#4a5a7c;
  --navy:#1c2340;
  --btn:#2b5486;
  --ink:#1b1b1b;
  --muted:#555;
  --light:#f7f7f7;
  --white:#fff;
  --star:#b5c21a;
  --accent:#2f5ea8;
}
*{margin:0;padding:0;box-sizing:border-box}
html,body{width:1200px;height:4601px;overflow:hidden}
body{font-family:'Poppins',sans-serif;color:var(--ink);background:var(--white);position:relative}
.abs{position:absolute}
.topbar{left:0;top:0;width:1200px;height:40px;background:var(--slate);color:#fff;font-size:16px}
.topbar .item{top:10px;display:flex;align-items:center;gap:8px}
.topbar .social{right:30px;top:12px;display:flex;gap:12px}
.topbar .social span{width:14px;height:14px;border-radius:50%;background:#fff;display:block}
.nav{left:0;top:40px;width:1200px;height:99px;background:#fff;border-bottom:1px solid #e4e4e4}
.nav a{position:absolute;top:42px;font-size:18px;font-weight:500;color:#333;text-decoration:none}
.brand{left:522px;top:14px;display:flex;align-items:center;gap:8px}
.brand .mark{width:70px;height:70px;border-radius:50%;border:5px solid var(--slate)}
.brand .name{font-size:17px;font-weight:600;color:var(--slate);line-height:1.1;width:120px}
.hero{left:0;top:139px;width:1200px;height:568px;background:linear-gradient(110deg,#2e3440 0%,#4d4a45 45%,#6a5a44 70%,#3a3b3f 100%)}
.hero-title{left:0;top:252px;width:1200px;text-align:center;color:#fff;font-size:52px;font-weight:800;line-height:1.13}
.hero-sub{left:0;top:438px;width:1200px;text-align:center;color:#fff;font-size:22px;line-height:1.2}
.btn-hero{left:446px;top:528px;width:297px;height:54px;background:var(--slate);color:#fff;font-size:19px;font-weight:500;display:flex;align-items:center;justify-content:center}
.light-band{left:0;top:707px;width:1200px;height:814px;background:var(--light)}
.feature{width:257px;height:219px;top:654px;background:#fff;border-radius:8px;box-shadow:0 2px 10px rgba(0,0,0,.12);text-align:center}
.feature svg{margin-top:16px}
.feature h3{font-size:16px;font-weight:600;margin-top:6px}
.feature p{font-size:8.5px;color:#666;line-height:1.8;margin-top:8px;text-transform:uppercase}
.feature .more{font-size:12px;font-weight:600;color:var(--slate);margin-top:10px;display:flex;justify-content:center;align-items:center;gap:8px}
.who-photo{left:75px;top:955px;width:489px;height:363px;background:linear-gradient(120deg,#6d4a38,#3c3b3e 55%,#8a6a52)}
.who-box{left:505px;top:1048px;width:561px;height:350px;background:#fff}
.who-box h2{position:absolute;left:48px;top:18px;font-size:27px;font-weight:700}
.who-box p{position:absolute;left:42px;top:67px;width:460px;font-size:12.5px;line-height:1.58;color:#444}
.btn-who{left:550px;top:1329px;width:217px;height:45px;background:var(--slate);color:#fff;font-size:13px;display:flex;align-items:center;justify-content:center;border-radius:3px}
.services{left:0;top:1521px;width:1200px;height:1127px;background:var(--slate)}
.sec-title{width:1200px;left:0;text-align:center;font-size:28px;font-weight:700}
.svc{width:267px;height:359px;background:#fff;border-radius:8px}
.svc .ph{position:absolute;left:16px;top:12px;width:235px;height:143px}
.svc .badge{position:absolute;left:48px;top:140px;width:60px;height:60px;border-radius:50%;background:var(--btn);border:4px solid #fff;display:flex;align-items:center;justify-content:center}
.svc h3{position:absolute;left:18px;top:212px;width:240px;font-size:16.5px;font-weight:600;line-height:1.2}
.svc p{position:absolute;left:18px;top:248px;width:235px;font-size:10px;line-height:1.3;color:#555}
.svc .more{position:absolute;left:18px;bottom:16px;font-size:9.5px;font-weight:600;color:var(--accent);display:flex;align-items:center;gap:6px}
.svc .more i{width:12px;height:12px;border-radius:50%;background:var(--accent);display:block}
.svc.two h3{top:200px}
.btn-all{left:491px;top:2527px;width:216px;height:45px;background:#fff;color:#333;font-size:13px;font-weight:500;display:flex;align-items:center;justify-content:center;border-radius:3px}
.testi{width:259px;height:271px;top:2809px;background:#fff;border-radius:18px;box-shadow:0 6px 16px rgba(0,0,0,.08);text-align:center}
.testi .avatar{width:66px;height:66px;border-radius:50%;background:linear-gradient(135deg,#8a6e5a,#3d4250);margin:14px auto 0}
.testi h4{font-size:17px;font-weight:600;margin-top:12px}
.testi p{font-size:11.5px;color:#555;line-height:1.6;margin:16px auto 0;width:200px}
.testi .stars{margin-top:14px;display:flex;justify-content:center;gap:6px}
.contact-band{left:0;top:3205px;width:1200px;height:924px;background:var(--light)}
.contact-photo{left:621px;top:3273px;width:490px;height:363px;background:linear-gradient(120deg,#6d4a38,#3c3b3e 55%,#8a6a52)}
.form-box{left:120px;top:3309px;width:560px;height:391px;background:#fff}
.form-box h2{position:absolute;left:45px;top:24px;font-size:28px;font-weight:700}
.field{position:absolute;background:#f6f6f6;border:1px solid #ececec;font-size:14px;color:#444;padding:8px 12px}
.btn-quote{position:absolute;left:109px;top:326px;width:347px;height:45px;background:var(--btn);color:#fff;font-size:13px;display:flex;align-items:center;justify-content:center;border-radius:3px}
.partner{top:3925px;height:116px}
.footer{left:0;top:4129px;width:1200px;height:472px;background:var(--navy);color:#fff}
.footer h5{position:absolute;top:66px;font-size:18px;font-weight:600}
.footer .about{position:absolute;left:29px;top:144px;width:280px;font-size:14px;line-height:2}
.footer .socials{position:absolute;left:29px;top:346px;display:flex;gap:12px}
.footer .socials span{width:40px;height:40px;border-radius:50%;background:#2d3d6b;display:block}
.fc{position:absolute;left:339px;font-size:14px;line-height:1.6}
.fc b{font-weight:600;display:block}
.fc svg{position:absolute;left:-1px;top:10px}
.fc div{margin-left:48px}
.ql{position:absolute;left:652px;width:264px;font-size:13px;border-bottom:1px solid #3a4262;height:42px;padding-top:12px}
.ql::after{content:"›";position:absolute;right:2px;top:8px;font-size:18px}
.oh{position:absolute;left:963px;font-size:14px;line-height:1.6}
.oh b{font-weight:600;display:block}
.oh i{position:absolute;left:0;top:8px;width:24px;height:24px;border-radius:50%;border:1.5px solid #8a93b0}
.oh div{margin-left:46px}
</style>
</head>
<body>

<header>
  <div class="abs topbar">
    <div class="abs item" style="left:60px">
      <svg width="16" height="12" viewBox="0 0 16 12"><rect width="16" height="12" rx="1" fill="#fff"/><path d="M0 1l8 6 8-6" stroke="#55678a" fill="none" stroke-width="1.4"/></svg>
      hello@kestrelworks.au
    </div>
    <div class="abs item" style="left:292px">
      <svg width="14" height="14" viewBox="0 0 24 24"><path fill="#fff" d="M6.6 10.8a15 15 0 006.6 6.6l2.2-2.2c.3-.3.7-.4 1-.2 1.1.4 2.3.6 3.6.6.6 0 1 .4 1 1V20c0 .6-.4 1-1 1C10.6 21 3 13.4 3 4c0-.6.4-1 1-1h3.5c.6 0 1 .4 1 1 0 1.3.2 2.5.6 3.6.1.3 0 .7-.2 1z"/></svg>
      (08) 5550 2741
    </div>
    <div class="abs social"><span></span><span></span><span></span></div>
  </div>
  <nav class="abs nav">
    <a style="left:63px">HOME</a>
    <a style="left:180px">ABOUT</a>
    <a style="left:309px">SERVICES</a>
    <div class="abs brand"><span class="mark"></span><span class="name">Kestrel Works Maintenance</span></div>
    <a style="left:740px">EQUIPMENTS</a>
    <a style="left:916px">CONTACT</a>
    <a style="left:1078px">BLOG</a>
  </nav>
</header>

<section>
  <div class="abs hero" role="img" aria-label="Technician in a hard hat working on heavy machinery"></div>
  <h1 class="abs hero-title">MECHANICAL<br>INSTRUMENTATION<br>SERVICES</h1>
  <p class="abs hero-sub">Lorem ipsum dolor sit amet, consectetuer adipiscing elit.<br>Aenean commodo ligula eget dolor.</p>
  <div class="abs btn-hero">GET STARTED TODAY</div>
</section>

<div class="abs light-band"></div>

<div class="abs feature" style="left:139px">
  <svg width="84" height="84" viewBox="0 0 84 84" fill="none" stroke="#55678a" stroke-width="3"><circle cx="42" cy="42" r="24"/><circle cx="42" cy="42" r="11"/><path d="M42 8v10M42 66v10M8 42h10M66 42h10M18 18l7 7M59 59l7 7M66 18l-7 7M25 59l-7 7"/></svg>
  <h3>Personalized Services</h3>
  <p>Lorem ipsum dolor sit amet,<br>consectetuer adipiscing elit.</p>
  <div class="more">READ MORE <svg width="26" height="10" viewBox="0 0 26 10"><path d="M0 5h20M16 1l6 4-6 4" stroke="#55678a" stroke-width="2.5" fill="none"/></svg></div>
</div>
<div class="abs feature" style="left:475px">
  <svg width="84" height="84" viewBox="0 0 84 84" fill="none" stroke="#55678a" stroke-width="3"><circle cx="42" cy="30" r="20"/><circle cx="42" cy="30" r="8"/><circle cx="24" cy="56" r="6"/><circle cx="42" cy="54" r="7"/><circle cx="60" cy="56" r="6"/><path d="M14 78v-8a10 10 0 0120 0v8M32 78v-8a10 10 0 0120 0v8M50 78v-8a10 10 0 0120 0v8"/></svg>
  <h3>Skilled Team</h3>
  <p>Lorem ipsum dolor sit amet,<br>consectetuer adipiscing elit.</p>
  <div class="more">READ MORE <svg width="26" height="10" viewBox="0 0 26 10"><path d="M0 5h20M16 1l6 4-6 4" stroke="#55678a" stroke-width="2.5" fill="none"/></svg></div>
</div>
<div class="abs feature" style="left:816px">
  <svg width="84" height="84" viewBox="0 0 84 84" fill="none" stroke="#55678a" stroke-width="3"><circle cx="42" cy="50" r="20"/><circle cx="42" cy="50" r="13"/><path d="M36 50l5 5 8-9"/><path d="M42 6l3 6 6 1-4 4 1 6-6-3-6 3 1-6-4-4 6-1z M18 16l2 4 4 1-3 3 1 4-4-2-4 2 1-4-3-3 4-1z M66 16l2 4 4 1-3 3 1 4-4-2-4 2 1-4-3-3 4-1z"/></svg>
  <h3>20+ Years of Experices</h3>
  <p>Lorem ipsum dolor sit amet,<br>consectetuer adipiscing elit.</p>
  <div class="more">READ MORE <svg width="26" height="10" viewBox="0 0 26 10"><path d="M0 5h20M16 1l6 4-6 4" stroke="#55678a" stroke-width="2.5" fill="none"/></svg></div>
</div>

<section>
  <div class="abs who-photo" role="img" aria-label="Mechanic in safety glasses servicing equipment in a workshop"></div>
  <div class="abs who-box">
    <h2>WHO WE ARE</h2>
    <p>Many business owners struggle to understand and maximize the true value of their businesses. This lack of awareness can lead to selling their business for less than it's worth, poor timing in the market, and inadequate preparation for the complexities of a business sale. They often face challenges in making their business attractive to buyers and aligning the sale with their personal and financial goals. This overall lack of preparedness and insight can result in significant financial and emotional regrets post-sale.</p>
  </div>
  <div class="abs btn-who">MORE ABOUT US</div>
</section>

<section>
  <div class="abs services"></div>
  <h2 class="abs sec-title" style="top:1575px;color:#fff">OUR SERVICES</h2>

  <div class="abs svc" style="left:121px;top:1682px">
    <div class="ph" role="img" aria-label="Worker inspecting a large red gearbox" style="background:linear-gradient(120deg,#8c1f22,#3b3f48 60%,#b5482f)"></div>
    <div class="badge"><svg width="30" height="30" viewBox="0 0 30 30" fill="none" stroke="#fff" stroke-width="2"><circle cx="15" cy="15" r="8"/><circle cx="15" cy="15" r="3"/><path d="M15 3v4M15 23v4M3 15h4M23 15h4"/></svg></div>
    <h3>Fixed Plant Repairs</h3>
    <p>Lorem ipsum dolor sit amet, consectetuer adipiscing elit. Aenean commodo ligula eget dolor. Aenean massa. Cum sociis natoque penatibus et magnis dis parturient montes, nascetur ridiculus mus.</p>
    <div class="more">READ MORE <i></i></div>
  </div>
  <div class="abs svc" style="left:466px;top:1682px">
    <div class="ph" role="img" aria-label="Yellow wheel loader on a worksite at sunset" style="background:linear-gradient(180deg,#c08a55,#7a6a4e 55%,#3e3a33)"></div>
    <div class="badge"><svg width="30" height="30" viewBox="0 0 30 30" fill="none" stroke="#fff" stroke-width="2"><rect x="6" y="12" width="14" height="8"/><path d="M10 12V7h6v5M20 16l5 4"/><circle cx="9" cy="23" r="2.5"/><circle cx="17" cy="23" r="2.5"/></svg></div>
    <h3>Earthmoving Equipment</h3>
    <p>Lorem ipsum dolor sit amet, consectetuer adipiscing elit. Aenean commodo ligula eget dolor. Aenean massa. Cum sociis natoque penatibus et magnis dis parturient montes, nascetur ridiculus mus.</p>
    <div class="more">READ MORE <i></i></div>
  </div>
  <div class="abs svc" style="left:811px;top:1682px">
    <div class="ph" role="img" aria-label="Mechanics working on a boat engine" style="background:linear-gradient(120deg,#2f3540,#6c7480 55%,#c9ccd0)"></div>
    <div class="badge"><svg width="30" height="30" viewBox="0 0 30 30" fill="none" stroke="#fff" stroke-width="2"><path d="M5 19h20l-3 6H8zM9 19v-6h12v6M15 13V6"/></svg></div>
    <h3>Large Boats</h3>
    <p>Lorem ipsum dolor sit amet, consectetuer adipiscing elit. Aenean commodo ligula eget dolor. Aenean massa. Cum sociis natoque penatibus et magnis dis parturient montes, nascetur ridiculus mus.</p>
    <div class="more">READ MORE <i></i></div>
  </div>

  <div class="abs svc two" style="left:121px;top:2084px">
    <div class="ph" role="img" aria-label="Engineers in hard hats reviewing a facility" style="background:linear-gradient(120deg,#c9c2b0,#d8c84a 40%,#3b3f46)"></div>
    <div class="badge"><svg width="30" height="30" viewBox="0 0 30 30" fill="none" stroke="#fff" stroke-width="2"><circle cx="15" cy="15" r="10"/><path d="M10 20l10-10M11 10l9 9"/></svg></div>
    <h3>Facilities Maintenance Services</h3>
    <p>Lorem ipsum dolor sit amet, consectetuer adipiscing elit. Aenean commodo ligula eget dolor. Aenean massa. Cum sociis natoque penatibus et magnis dis parturient montes, nascetur ridiculus mus.</p>
    <div class="more">READ MORE <i></i></div>
  </div>
  <div class="abs svc" style="left:466px;top:2084px">
    <div class="ph" role="img" aria-label="Welding sparks in a fabrication workshop" style="background:radial-gradient(circle at 55% 55%,#e8f0ff,#5f7fb0 30%,#1d2330 75%)"></div>
    <div class="badge"><svg width="30" height="30" viewBox="0 0 30 30" fill="none" stroke="#fff" stroke-width="2"><rect x="6" y="6" width="18" height="18"/><circle cx="15" cy="15" r="4"/></svg></div>
    <h3>Workshop Fabrication</h3>
    <p>Lorem ipsum dolor sit amet, consectetuer adipiscing elit. Aenean commodo ligula eget dolor. Aenean massa. Cum sociis natoque penatibus et magnis dis parturient montes, nascetur ridiculus mus.</p>
    <div class="more">READ MORE <i></i></div>
  </div>
  <div class="abs svc two" style="left:811px;top:2084px">
    <div class="ph" role="img" aria-label="Stainless steel tanks and pipework in a processing plant" style="background:linear-gradient(90deg,#b8bec4,#e3e6e9 40%,#8d949c)"></div>
    <div class="badge"><svg width="30" height="30" viewBox="0 0 30 30" fill="none" stroke="#fff" stroke-width="2"><rect x="6" y="8" width="7" height="16"/><rect x="17" y="12" width="7" height="12"/><path d="M13 14h4"/></svg></div>
    <h3>Chemical Processing Facilities</h3>
    <p>Lorem ipsum dolor sit amet, consectetuer adipiscing elit. Aenean commodo ligula eget dolor. Aenean massa. Cum sociis natoque penatibus et magnis dis parturient montes, nascetur ridiculus mus.</p>
    <div class="more">READ MORE <i></i></div>
  </div>

  <div class="abs btn-all">VIEW ALL SERVICES</div>
</section>

<section>
  <h2 class="abs sec-title" style="top:2718px;left:-24px">WHAT OUR CLIENT SAYS</h2>
  <div class="abs testi" style="left:125px">
    <div class="avatar" role="img" aria-label="Client portrait"></div>
    <h4>Sam Porter</h4>
    <p>Lorem ipsum dolor sit amet, consectetur adipiscing elit, sed do eiusmod tempor incididunt ut labore et dolore magna aliqua.</p>
    <div class="stars"><svg width="140" height="22" viewBox="0 0 140 22" fill="#b5c21a"><g id="st"><polygon points="11,1 14,8 21,8 15.5,13 17.5,21 11,16.5 4.5,21 6.5,13 1,8 8,8"/></g><use href="#st" x="29"/><use href="#st" x="58"/><use href="#st" x="87"/><use href="#st" x="116"/></svg></div>
  </div>
  <div class="abs testi" style="left:454px">
    <div class="avatar" role="img" aria-label="Client portrait"></div>
    <h4>Sam Porter</h4>
    <p>Lorem ipsum dolor sit amet, consectetur adipiscing elit, sed do eiusmod tempor incididunt ut labore et dolore magna aliqua.</p>
    <div class="stars"><svg width="140" height="22" viewBox="0 0 140 22" fill="#b5c21a"><use href="#st"/><use href="#st" x="29"/><use href="#st" x="58"/><use href="#st" x="87"/><use href="#st" x="116"/></svg></div>
  </div>
  <div class="abs testi" style="left:782px">
    <div class="avatar" role="img" aria-label="Client portrait"></div>
    <h4>Sam Porter</h4>
    <p>Lorem ipsum dolor sit amet, consectetur adipiscing elit, sed do eiusmod tempor incididunt ut labore et dolore magna aliqua.</p>
    <div class="stars"><svg width="140" height="22" viewBox="0 0 140 22" fill="#b5c21a"><use href="#st"/><use href="#st" x="29"/><use href="#st" x="58"/><use href="#st" x="87"/><use href="#st" x="116"/></svg></div>
  </div>
</section>

<section>
  <div class="abs contact-band"></div>
  <div class="abs contact-photo" role="img" aria-label="Mechanic servicing equipment in a workshop"></div>
  <div class="abs form-box">
    <h2>CONTACT US NOW</h2>
    <div class="field" style="left:48px;top:81px;width:226px;height:35px">Name</div>
    <div class="field" style="left:290px;top:81px;width:226px;height:35px">Email</div>
    <div class="field" style="left:48px;top:133px;width:226px;height:35px">Phone</div>
    <div class="field" style="left:290px;top:133px;width:226px;height:35px">Service</div>
    <div class="field" style="left:48px;top:185px;width:468px;height:114px">Message</div>
    <div class="btn-quote">REQUEST A QUOTE NOW</div>
  </div>

  <h2 class="abs sec-title" style="top:3812px">OUR PARTNERS</h2>
  <div class="abs partner" style="left:107px;top:3963px;width:118px;height:42px;background:#d8262e"></div>
  <div class="abs partner" style="left:268px;top:3930px;width:120px;height:106px;border-radius:50%;background:#c9c2b4"></div>
  <div class="abs partner" style="left:428px;width:111px;background:#1e4f9a"></div>
  <div class="abs partner" style="left:589px;top:3930px;width:106px;height:106px;border-radius:50%;background:#c7262c"></div>
  <div class="abs partner" style="left:741px;width:118px;background:#3a3d9a"></div>
  <div class="abs partner" style="left:899px;top:3960px;width:224px;height:46px;background:#b8c2cf"></div>
</section>

<footer class="abs footer">
  <h5 style="left:29px">ABOUT US</h5>
  <p class="about">We are an award winning plumbing company with over 20 years experience in the business. We provide a wide range of services for both residential and commercial clients.</p>
  <div class="socials"><span></span><span></span><span></span></div>

  <h5 style="left:339px">CONTACT US</h5>
  <div class="fc" style="top:140px"><svg width="24" height="24" viewBox="0 0 24 24" fill="none" stroke="#8a93b0" stroke-width="1.5"><path d="M12 22s7-7 7-12a7 7 0 00-14 0c0 5 7 12 7 12z"/><circle cx="12" cy="10" r="2.5"/></svg><div><b>Address:</b>18 Foundry Lane, Welshpool WA</div></div>
  <div class="fc" style="top:214px"><svg width="24" height="24" viewBox="0 0 24 24" fill="none" stroke="#8a93b0" stroke-width="1.5"><rect x="3" y="7" width="18" height="12" rx="2"/><path d="M7 7V5h10v2"/></svg><div><b>Phone:</b>+61 8 5550 2741</div></div>
  <div class="fc" style="top:288px"><svg width="24" height="24" viewBox="0 0 24 24" fill="none" stroke="#8a93b0" stroke-width="1.5"><rect x="7" y="2" width="10" height="20" rx="2"/></svg><div><b>Mobile:</b>+61 8 5550 2741</div></div>
  <div class="fc" style="top:362px"><svg width="24" height="24" viewBox="0 0 24 24" fill="none" stroke="#8a93b0" stroke-width="1.5"><rect x="2" y="5" width="20" height="14" rx="1"/><path d="M2 6l10 7 10-7"/></svg><div><b>Email:</b>support@kestrelworks.au</div></div>

  <h5 style="left:652px">QUICK LINKS</h5>
  <div class="ql" style="top:132px">About</div>
  <div class="ql" style="top:174px">Contact</div>
  <div class="ql" style="top:216px">News List</div>
  <div class="ql" style="top:258px">Services</div>
  <div class="ql" style="top:300px;border-bottom:none">Shop</div>

  <h5 style="left:963px">OPENING HOURS</h5>
  <div class="oh" style="top:138px"><i></i><div><b>Monday - Friday</b>8:00 AM - 5:00 PM</div></div>
  <div class="oh" style="top:212px"><i></i><div><b>Saturday</b>9:00 AM - 4:00 PM</div></div>
  <div class="oh" style="top:286px"><i></i><div><b>Sunday</b>CLOSED</div></div>
</footer>

</body>
</html>
```